Pet label template for Valdemoro mexican based company

Hello, Valdemoro is a mexican based company dedicated to manufacture and sell its propietary brands for human health care. We are now introducing a new "Pet" category to our Brand. It´s name is Valdemoro Pets (logo attached).
We are lookoig for the design template for our package labels that will most probably be in plastic bags like the example attaches (Furwell Organics of Tasco). It is important to point out that the labels are going to be pasted on the bags and not directly printed on the bags itself like the examples attached.

I am attaching some examples but please feel free to innovate your own desing. I am also attaching the logo that must be in every label.

Target Market(s)

Pet owners basically dogs and cats.

Industry/Entity Type

Health Care

Font styles to use
Other font styles liked:
• something easy to read

Requirements
Must have
• We like both simple elegant designs and bright colorful ones son feel free to innovate.
Nice to have
• Illustration of both cat or dog for their product label.

```html
<!DOCTYPE html>
<html lang="en">
<head>
<meta charset="utf-8">
<title>Veterinarian Formulated Supplement Labels</title>
<link rel="stylesheet" href="https://fonts.googleapis.com/css2?family=Fredoka:wght@600&family=Quicksand:wght@400;500&display=swap">
<style>
  :root {
    --canvas: #ffffff;
    --label-edge: #b1b2b5;
    --label-mid: #dcdcde;
    --label-center: #ffffff;
    --cat-blue: #0fa3d2;
    --dog-orange: #f7941d;
    --body-white: #ffffff;
    --photo-light: #c9c9cb;
    --photo-dark: #6f6f72;
    --photo-black: #2a2a2c;
  }
  html, body {
    margin: 0;
    padding: 0;
    width: 1200px;
    height: 919px;
    overflow: hidden;
    background: var(--canvas);
  }
  .sheet {
    position: relative;
    width: 1200px;
    height: 919px;
  }
  .label {
    position: absolute;
    top: 130px;
    width: 500px;
    height: 656px;
    border-radius: 24px;
    overflow: hidden;
    background: radial-gradient(ellipse 70% 55% at 50% 48%, var(--label-center) 0%, var(--label-mid) 60%, var(--label-edge) 100%);
    box-shadow: 0 2px 6px rgba(0,0,0,0.18);
  }
  .label--cats { left: 70px; --accent: var(--cat-blue); }
  .label--dogs { left: 630px; --accent: var(--dog-orange); }

  .label__tagline {
    position: absolute;
    left: 36px;
    top: 58px;
    margin: 0;
    font-family: "Quicksand", sans-serif;
    font-weight: 500;
    font-size: 34px;
    letter-spacing: 0.5px;
    color: var(--accent);
    white-space: nowrap;
  }
  .label__title {
    position: absolute;
    left: 34px;
    top: 112px;
    margin: 0;
    font-family: "Fredoka", sans-serif;
    font-weight: 600;
    color: var(--accent);
    line-height: 1;
    white-space: nowrap;
  }
  .label__title-line { display: block; }
  .label__title-line--top { font-size: 61px; letter-spacing: 1px; }
  .label__title-line--bottom { font-size: 80px; margin-top: 4px; letter-spacing: 1px; }

  .label__photo {
    position: absolute;
    left: 290px;
    top: 262px;
    width: 178px;
    height: 260px;
  }
  .label--cats .label__photo {
    background: linear-gradient(180deg, var(--photo-light) 0%, var(--photo-dark) 100%);
  }
  .label--dogs .label__photo {
    background: linear-gradient(180deg, var(--photo-dark) 0%, var(--photo-black) 100%);
  }

  .label__band {
    position: absolute;
    left: 0;
    top: 0;
    width: 500px;
    height: 656px;
  }
  .label__band path { fill: var(--accent); }

  .label__body {
    position: absolute;
    left: 40px;
    right: 40px;
    top: 548px;
    margin: 0;
    font-family: "Quicksand", sans-serif;
    font-weight: 500;
    font-size: 12.5px;
    line-height: 1.4;
    text-align: center;
    color: var(--body-white);
  }
</style>
</head>
<body>
<main class="sheet">

  <section class="label label--cats">
    <p class="label__tagline">veterinarian formulated</p>
    <h1 class="label__title">
      <span class="label__title-line label__title-line--top">SUPPLEMENT</span>
      <span class="label__title-line label__title-line--bottom">FOR CATS</span>
    </h1>
    <div class="label__photo" role="img" aria-label="Photo of a grey tabby cat licking its lips"></div>
    <svg class="label__band" viewBox="0 0 500 656" aria-hidden="true">
      <path d="M0 412 Q250 616 500 412 L500 656 L0 656 Z"/>
    </svg>
    <p class="label__body">Sed ut perspiciatis unde omnis iste natus error sit voluptatem accusantium doloremque laudantium, totam rem aperiam, eaque ipsa quae ab illo inventore veritatis et quasi architecto beatae vitae dicta sunt explicabo.</p>
  </section>

  <section class="label label--dogs">
    <p class="label__tagline">veterinarian formulated</p>
    <h2 class="label__title">
      <span class="label__title-line label__title-line--top">SUPPLEMENT</span>
      <span class="label__title-line label__title-line--bottom">FOR DOGS</span>
    </h2>
    <div class="label__photo" role="img" aria-label="Photo of a black long-haired dog licking its nose"></div>
    <svg class="label__band" viewBox="0 0 500 656" aria-hidden="true">
      <path d="M0 412 Q250 616 500 412 L500 656 L0 656 Z"/>
    </svg>
    <p class="label__body">Sed ut perspiciatis unde omnis iste natus error sit voluptatem accusantium doloremque laudantium, totam rem aperiam, eaque ipsa quae ab illo inventore veritatis et quasi architecto beatae vitae dicta sunt explicabo.</p>
  </section>

</main>
</body>
</html>
```